Lumen QRX - Website

Lumen QRX is a online marketing solutions Agency, working with top partners within the industry to deliver online customers to Digital campaigns.

Our current site is www.lumenqrx-example.com (Apart from the logo, there is NOTHING we like about this site - please do not repeat anything from this site)

Specification of website:

- Modern, and light refreshing look. Corporate and neutral designs.

-Keep our logo - colour theme: Green/grey - hint of Orange/Blue

- The only text we would like on the Homepage is: Performance based online marketing specialists, driving incremental sales globally

and...

These are headings we would like people to do: Affiliate Marketing, Email marketing, Lead Generation, Social media marketing, Search Engine Marketing, Incentive Marketing (there is no need for the detailed text of these topics to be on front page, these can be linked into another page for those who seeks further info)

Images: Have images to show what we do.. keep it neat and professional/simple and stylish.

Please contact us if you have any questions at all.

Thank you for taking time our with our project!

Good luck all!

Regards

Lumen QRX
Updates

Hello Designers,

Thank you to all who have taken time out working on our project. We have been very happy with the quality and level of prompt feedback.

Unfortunately we could only choose one, and VelBoro's designed is most suited for our company branding. So, Congratulations VelBoro.

Once again, thank you all.

Kindest regards,

Lumen QRX

Target Market(s)

Clients: Fizzo, Torvik, Lunto, panelo.example, Brevard Hotel...

Industry/Entity Type

Marketing

Requirements
Must have
• User friendly
Nice to have
• We operate Internationally, so a generic feel for EU/UK/US would be ideal...
Should not have
• Should not look like www.lumenqrx-example.com

```html
<!DOCTYPE html>
<html lang="en">
<head>
<meta charset="utf-8">
<title>Lumen QRX – Performance Based Online Marketing</title>
<link rel="stylesheet" href="https://fonts.googleapis.com/css2?family=Yanone+Kaffeesatz:wght@400;500;600&family=Ubuntu:wght@400;500;700&family=PT+Sans:wght@400;700&display=swap">
<style>
:root{
  --green-deep:#4d6f1c;
  --green-mid:#7fa235;
  --green-light:#b6cf6a;
  --nav-band:rgba(70,95,40,.78);
  --nav-text:#d9f20f;
  --brand-green:#5f9a1e;
  --brand-dark:#3f6a12;
  --ink:#2a2a2a;
  --services-bg:#f2f2f2;
  --sky:#a0effa;
  --sky-edge:#7fcfdd;
  --cream:#fdfcf4;
  --white:#ffffff;
}
*{box-sizing:border-box;margin:0;padding:0}
html,body{width:1187px;height:1200px;overflow:hidden}
body{font-family:"PT Sans",sans-serif;color:var(--ink);background:var(--cream)}
.canvas{position:relative;width:1187px;height:1200px;overflow:hidden}
.abs{position:absolute}

/* header */
.masthead{left:0;top:0;width:1187px;height:389px;
  background:radial-gradient(ellipse at 15% 70%,var(--green-light) 0%,transparent 45%),
             radial-gradient(ellipse at 85% 80%,#c7da7d 0%,transparent 40%),
             linear-gradient(180deg,var(--green-mid) 0%,#8fb23f 55%,var(--green-deep) 100%)}
.nav-band{left:0;top:0;width:1187px;height:60px;background:var(--nav-band);border-bottom:1px solid #9bbb55}
.nav-item{top:22px;font-family:"Ubuntu",sans-serif;font-size:16.5px;color:var(--nav-text)}
.nav-home{left:205px;top:15px;width:111px;height:37px;border-radius:18px;background:var(--white);
  border:3px solid #3e4a35;color:#111;font-family:"Ubuntu",sans-serif;font-size:17px;text-align:center;line-height:31px}

.hero{left:123px;top:64px;width:946px;height:304px;background:linear-gradient(90deg,#f4f4f4 0%,#efefef 60%,#e9eef3 100%);border:1px solid #ddd}
.hero-visual{left:760px;top:65px;width:310px;height:300px;
  background:radial-gradient(circle at 55% 42%,#bfe9fb 0%,#55a8dc 25%,rgba(210,230,240,.5) 45%,transparent 65%),
             linear-gradient(180deg,#eef3f6,#e4eaee);border-bottom-right-radius:110px}
.brand{left:145px;top:100px;font-family:"PT Sans",sans-serif;font-weight:700;font-size:44px;line-height:50px;color:var(--brand-dark)}
.tagline{left:145px;top:193px;font-family:"Yanone Kaffeesatz",sans-serif;font-weight:500;font-size:24px;line-height:28px;color:var(--brand-dark);white-space:nowrap}
.tagline .accent{color:var(--brand-green)}
.intro{left:146px;top:236px;width:545px;font-size:11px;line-height:16px;color:#222}

/* services */
.services{left:0;top:389px;width:1187px;height:334px;background:var(--services-bg)}
.service-box{left:131px;top:420px;width:939px;height:274px;background:var(--sky);border:1px solid var(--sky-edge);border-radius:10px}
.col-rule{top:450px;width:1px;height:228px;background:#c4f6fd}
.service-title{width:200px;font-family:"Yanone Kaffeesatz",sans-serif;font-weight:500;font-size:19px;color:#111;text-align:center;top:433px}
.service-thumb{top:459px;width:187px;height:70px;border:1px solid #8ab;border-radius:8px}
.service-text{top:536px;width:182px;font-size:11px;line-height:16px;color:#333}
.read-more{font-size:11px;color:#222;display:flex;align-items:center;gap:4px}
.read-more svg{width:9px;height:9px}

/* features */
.feature-card{top:744px;width:226px;height:95px;background:var(--white);border:1px solid #ccc;box-shadow:0 1px 3px rgba(0,0,0,.2);padding:5px}
.feature-image{position:relative;width:214px;height:83px}
.feature-caption{position:absolute;left:0;bottom:0;width:100%;height:30px;background:rgba(40,40,40,.7);
  font-family:"Yanone Kaffeesatz",sans-serif;font-size:18px;color:#fff;padding:4px 7px;white-space:nowrap}
.feature-text{top:850px;width:228px;font-size:11px;line-height:16px;color:#333}

/* footer */
.footer{left:0;top:1008px;width:1187px;height:192px;
  background:radial-gradient(ellipse at 10% 80%,#d7e59a 0%,transparent 40%),
             linear-gradient(180deg,#8fb043 0%,#a7c558 50%,#7c9f33 100%)}
.footer-links{left:205px;top:1077px;width:480px;text-align:center;font-family:"Ubuntu",sans-serif;font-weight:700;font-size:11.5px;color:#fff;line-height:18px}
.footer-links .sep{margin:0 9px}
.contact-card{left:775px;top:1032px;width:294px;height:143px;border-radius:12px;border:1px solid #5d7a2f;overflow:hidden;
  background:linear-gradient(90deg,#d9f0cf 0%,#c7e6c0 55%,#7d8f6a 100%);font-style:normal}
.contact-photo{right:0;top:0;width:140px;height:143px;background:linear-gradient(90deg,rgba(220,235,215,0) 0%,#c8a58e 45%,#5a3b2c 100%)}
.contact-body{left:12px;top:8px;font-family:"Ubuntu",sans-serif;font-size:12.5px;line-height:18px;color:#111}
.contact-title{font-family:"Yanone Kaffeesatz",sans-serif;font-weight:500;font-size:24px;line-height:30px;color:var(--brand-dark)}
</style>
</head>
<body>
<div class="canvas">

  <header class="masthead abs"></header>
  <nav class="nav-band abs" aria-label="Main">
    <span class="nav-home abs">Home</span>
    <span class="nav-item abs" style="left:336px">About Us</span>
    <span class="nav-item abs" style="left:458px">What We Do</span>
    <span class="nav-item abs" style="left:605px">Our Work</span>
    <span class="nav-item abs" style="left:730px">Work With Us</span>
    <span class="nav-item abs" style="left:885px">Contacts</span>
  </nav>

  <section class="hero abs"></section>
  <div class="hero-visual abs" role="img" aria-label="Hand holding a glowing blue globe on a curling page"></div>
  <div class="brand abs">Lumen QRX</div>
  <h1 class="tagline abs">Performance based <span class="accent">online</span> marketing specialists<span class="accent">, driving incremental sales globally</span></h1>
  <p class="intro abs">Lorem ipsum dolor sit amet, consectetur adipiscing elit. Ut aliquet lacus et dolor mollis bibendum. Mauris sodales magna vel erat porttitor vel hendrerit velit lacinia. Vestibulum neque libero, placerat eget sagittis vel, vulputate eget lectus. Nullam tortor libero, dapibus tempus elementum id, feugiat vel odio. Proin in orci quis ipsum hendrerit mattis. Nullam lectus odio, venenatis at laoreet non, consectetur id massa.</p>

  <section class="services abs"></section>
  <div class="service-box abs"></div>
  <div class="col-rule abs" style="left:358px"></div>
  <div class="col-rule abs" style="left:599px"></div>
  <div class="col-rule abs" style="left:839px"></div>

  <h2 class="service-title abs" style="left:133px">Email Marketing</h2>
  <div class="service-thumb abs" style="left:141px;background:linear-gradient(90deg,#4a78b8,#dfe6ec 45%,#f2f2f2 60%,#d9a43a)" role="img" aria-label="Globe with envelope and people icons"></div>
  <p class="service-text abs" style="left:145px">People aged between 18 and 24 spend an average of 31 hours a month checking their inboxes. Study has shown that email marketing will remain an essential tool in marketing for a long time to come.</p>
  <a class="read-more abs" style="left:148px;top:648px"><svg viewBox="0 0 9 9"><rect width="9" height="9" fill="#111"/><path d="M2 2l5 5M7 3v4H3" stroke="#fff" fill="none"/></svg>Read More</a>

  <h2 class="service-title abs" style="left:377px">Lead Generation</h2>
  <div class="service-thumb abs" style="left:385px;background:linear-gradient(90deg,#9d8570,#d8cfc6 40%,#f5f5f5)" role="img" aria-label="Man working at a laptop"></div>
  <p class="service-text abs" style="left:389px">This channel remains one of the most powerful acquisition methods in marketing. At Lumen QRX we understand that to harness the true power of lead gen you have to balance quantity with quality.</p>
  <a class="read-more abs" style="left:391px;top:648px"><svg viewBox="0 0 9 9"><rect width="9" height="9" fill="#111"/><path d="M2 2l5 5M7 3v4H3" stroke="#fff" fill="none"/></svg>Read More</a>

  <h2 class="service-title abs" style="left:619px">Incentive Marketing</h2>
  <div class="service-thumb abs" style="left:627px;background:linear-gradient(180deg,#ffffff,#e2e2e2)" role="img" aria-label="Rising bar chart with an arrow"></div>
  <p class="service-text abs" style="left:631px">It is a $46bn+ a year industry because it drives very high volumes of traffic at low costs and should never be ruled out without careful consideration.</p>
  <a class="read-more abs" style="left:634px;top:648px"><svg viewBox="0 0 9 9"><rect width="9" height="9" fill="#111"/><path d="M2 2l5 5M7 3v4H3" stroke="#fff" fill="none"/></svg>Read More</a>

  <h2 class="service-title abs" style="left:863px">Social Media Marketing</h2>
  <div class="service-thumb abs" style="left:870px;background:radial-gradient(circle at 55% 50%,#9fdcff 0%,#1f63c0 35%,#071d55 80%)" role="img" aria-label="Glowing globe with web lettering"></div>
  <p class="service-text abs" style="left:874px">Lumen QRX and its partners have consistently been at the forefront of this new media, helping to pioneer new monetisation methods and strategies.</p>
  <a class="read-more abs" style="left:877px;top:648px"><svg viewBox="0 0 9 9"><rect width="9" height="9" fill="#111"/><path d="M2 2l5 5M7 3v4H3" stroke="#fff" fill="none"/></svg>Read More</a>

  <div class="feature-card abs" style="left:132px">
    <div class="feature-image" style="background:linear-gradient(90deg,#9fb0c0,#d8d2c8 50%,#8a7d70)" role="img" aria-label="Business team in an office">
      <span class="feature-caption">Search Engine Marketing</span></div>
  </div>
  <p class="feature-text abs" style="left:133px">Global SEM spend projected to increase to $31.6bn by 2014. Our in-house team of 'Search specialists' and network covers tens of thousands of sites in the UK, Continental Europe, North America and beyond.</p>
  <a class="read-more abs" style="left:134px;top:944px"><svg viewBox="0 0 9 9"><rect width="9" height="9" fill="#111"/><path d="M2 2l5 5M7 3v4H3" stroke="#fff" fill="none"/></svg>Read More</a>

  <div class="feature-card abs" style="left:368px">
    <div class="feature-image" style="background:linear-gradient(90deg,#eeeae4,#c9c2b8 55%,#5a4c44)" role="img" aria-label="Clock face with a running figure">
      <span class="feature-caption">Search Engine Optimization</span></div>
  </div>
  <p class="feature-text abs" style="left:369px">It is vital that both channels, organic and paid search results optimises your brand and online presence. We offer full services from analysis of websites to comprehensive campaign planning, managing and reporting.</p>
  <a class="read-more abs" style="left:370px;top:944px"><svg viewBox="0 0 9 9"><rect width="9" height="9" fill="#111"/><path d="M2 2l5 5M7 3v4H3" stroke="#fff" fill="none"/></svg>Read More</a>

  <div class="feature-card abs" style="left:604px">
    <div class="feature-image" style="background:linear-gradient(100deg,#e0303a,#f08a20 25%,#f3e11a 45%,#4fc23a 65%,#2b8fd8 90%)" role="img" aria-label="Row of colourful markers">
      <span class="feature-caption">Custom Web Design</span></div>
  </div>
  <p class="feature-text abs" style="left:606px">If a larger scale website, multimedia or a digital strategy is required, we have worldwide connections to make sure that the project is made to fit the ideas of the client.</p>
  <a class="read-more abs" style="left:607px;top:944px"><svg viewBox="0 0 9 9"><rect width="9" height="9" fill="#111"/><path d="M2 2l5 5M7 3v4H3" stroke="#fff" fill="none"/></svg>Read More</a>

  <div class="feature-card abs" style="left:842px">
    <div class="feature-image" style="background:linear-gradient(90deg,#2a1e18,#6b5447 45%,#c8ccd0 65%,#2b2522)" role="img" aria-label="Hand pressing a calculator keypad">
      <span class="feature-caption">Account Management</span></div>
  </div>
  <p class="feature-text abs" style="left:843px">Communication is the key to success of any relationship and online marketing is no exception. We believe that client interaction and discussion is the only way to enable the free flow of ideas.</p>
  <a class="read-more abs" style="left:844px;top:944px"><svg viewBox="0 0 9 9"><rect width="9" height="9" fill="#111"/><path d="M2 2l5 5M7 3v4H3" stroke="#fff" fill="none"/></svg>Read More</a>

  <footer class="footer abs"></footer>
  <div class="footer-links abs">
    Home<span class="sep">|</span>About Us<span class="sep">|</span>What We Do<span class="sep">|</span>Our Work<span class="sep">|</span>Work With Us<span class="sep">|</span>Contact Us<br>
    Copyright © 2010 Lumen QRX. All Rights Reserved.<br>
    Powered by LUMEN QRX
  </div>
  <address class="contact-card abs">
    <div class="contact-photo abs" role="img" aria-label="Support agent wearing a headset"></div>
    <div class="contact-body abs">
      <div class="contact-title">Lumen QRX</div>
      48 Corwen Lane<br>London E9 4TX<br>United Kingdom.<br>Phone - +44 (0)7700900418<br>fax +44 (0) 207 946 0152
    </div>
  </address>

</div>
</body>
</html>
```